Online Music Gear Store needs Business Cards

We need BC designs for our e-commerce for meetings and networking
we are an Online Store and we sell Audio and Music Equipment and Gear
we also provide EVENTUAL Audio and Music Production services but our core service is the Online Store: Selling Premium Brands

we are based in Tijuana and San Diego CA.
our brand/name is: Vellmoor

our name comes from the early tape machines that the Corvanes and many other early day artist used to record with to do their magnificent masterpieces.

Now in 2014 we can have Amazing Studio-Quality Multitrack sessions with a few pieces of Gear and an Slatepod... For example, you can only have your Pocketline and an Brisa Tandem to start recording using Loft Deck for Quorix.

If the best bands from the early days had to use million dollar recording studios with very expensive gear such as 4-track tape machines... now you can achieve better sounding results in your bedroom, using the gear we sell.

Thats what we try to Communicate with the Name:

That you... a young musician can start doing multitrack sessions using the Best Gear with the Latest Technology and compatible with Trelons, Quorix devices:

Example of the Premium Brands we sell are:
Brisa, ZQ Mediaworks

we want to communicate (even if we are an ecommerce and a startup) that we are Serious, and Very Elegant, Sophisticated and Minimal.

that we provide Complete solutions, the best gear... the best brands... that we also do our productions with the best gear, best brands and very important we are Pomeroy ONLY, Trelons Only

examples of the brands we sell are Kolbrandt, Brisa, ZQ Mediaworks, Rolf Ingham Instruments, Arc 9. Our focus is Music Technology.
we also use Cadence Max Q.

Our favorite colors are black, white, grey, silver, orange, blue, green, maybe bit of yellow.

No need to use all of them but you can combine. At the end you can use Color Theory to achieve assertive communication.

Target Market(s)

CEO's, VP's, VC's, Sales People, High Class executives...
Purchasing Departments, and Corporations.

Industry/Entity Type

E-Commerce

Requirements
Must have
• Should include:

1. Logo
2. website,
3. Managing Director Info:
4. Minimal and Elegant/Upper Class

feel free to suggest ideas, feel free to play around with logo and fonts as well... since we are not 100% happy with our logo...

must also show that we are Pomeroy and Trelon only in a way without being obvious or without showing Pomeroy Logo

we need to have at the end of the project the .AI
.PSD and any related designed file to edit in the future, logo, numbers, etc...

my info:

Tomas Emil Varga-Lindqvist
Vellmoor | Mexico City, Tijuana, San Diego,
Chatterbox | Peeplo | Zenbo+ | Clipwall | Snapframe ???? (what do you thing about this links ???) too much ???
Mobile: +5219987350418 | 0115219987350418
USA Number: 1-800-572-9183
VuCall & QuickNote: studio@vellmoor-example.mx
Talkwave: studiovellmoormx
Should not have
• it shouldn't use our real address, but should imply that we are in Mexico City, in Tijuana and San Diego CA.

Should not use the Pomeroy Logo (even if we are Pomeroy only)

should not have Robotix or PC/Panelix related designs.

```html
<!DOCTYPE html>
<html lang="en">
<head>
<meta charset="utf-8">
<title>Vellmoor business cards</title>
<link href="https://fonts.googleapis.com/css2?family=Didact+Gothic&display=swap" rel="stylesheet">
<style>
  :root {
    --bg: #d9d9d6;
    --black: #0b0b0b;
    --charcoal: #1c1c1c;
    --silver: #cfcfcf;
    --white: #ffffff;
    --orange: #f39a1e;
    --blue: #1a73c9;
    --blue-deep: #2438a6;
    --green: #8cc63f;
    --ink: #111111;
  }
  * { box-sizing: border-box; margin: 0; padding: 0; }
  html, body { width: 1200px; height: 1026px; overflow: hidden; }
  body {
    background: var(--bg);
    font-family: "Didact Gothic", "Century Gothic", sans-serif;
    position: relative;
  }
  .card { position: absolute; overflow: hidden; box-shadow: 0 10px 28px rgba(0,0,0,.35); }

  /* Front card */
  .card-front {
    left: 60px; top: 70px; width: 540px; height: 820px;
    background: radial-gradient(ellipse at 50% 35%, var(--charcoal), var(--black) 75%);
    color: var(--white); text-align: center;
  }
  .card-front .front-lines { position: absolute; inset: 0; }
  .front-wordmark {
    position: absolute; left: 0; right: 0; top: 250px;
    font-size: 76px; color: var(--silver); letter-spacing: 1px;
  }
  .front-mark-dot {
    position: absolute; left: 50%; top: 110px; width: 110px; height: 110px;
    margin-left: -55px; border-radius: 50%; background: var(--silver);
  }
  .front-cities {
    position: absolute; left: 0; right: 0; top: 468px;
    font-size: 21px; letter-spacing: 1px;
  }
  .front-cities span + span { border-left: 2px solid var(--white); padding-left: 6px; margin-left: 4px; }
  .front-follow {
    position: absolute; left: 0; right: 0; top: 560px;
    color: var(--orange); font-size: 25px; letter-spacing: 2px;
  }
  .social-list {
    position: absolute; left: 30px; right: 30px; top: 620px;
    display: flex; justify-content: center; gap: 18px; list-style: none;
    font-size: 19px; color: var(--white);
  }

  /* Back card */
  .card-back {
    left: 640px; top: 200px; width: 500px; height: 760px;
    background: var(--white); text-align: center; color: var(--ink);
  }
  .card-back .back-frame { position: absolute; inset: 0; }
  .back-mark-dot {
    position: absolute; left: 50%; top: 110px; width: 90px; height: 90px;
    margin-left: -45px; border-radius: 50%; background: var(--green);
  }
  .back-wordmark {
    position: absolute; left: 0; right: 0; top: 235px;
    font-size: 56px; color: var(--ink);
  }
  .person-name {
    position: absolute; left: 0; right: 0; top: 400px;
    color: var(--orange); font-size: 32px; letter-spacing: 1px;
  }
  .person-surname {
    position: absolute; left: 0; right: 0; top: 446px; font-size: 21px;
  }
  .divider {
    position: absolute; left: 160px; width: 180px; height: 2px; background: var(--green);
  }
  .contact-line { position: absolute; left: 0; right: 0; font-size: 21px; }
  .contact-line .label { color: var(--orange); }
  .contact-small { font-size: 17px; }
  .phone-icon { display: inline-block; vertical-align: -3px; margin-right: 3px; }
</style>
</head>
<body>

<section class="card card-front" aria-label="Card front">
  <svg class="front-lines" width="540" height="820" aria-hidden="true">
    <path d="M60 0 C20 300 100 500 40 820" stroke="#2a2a2a" stroke-width="2" fill="none"/>
    <path d="M480 0 C520 300 440 500 500 820" stroke="#2a2a2a" stroke-width="2" fill="none"/>
  </svg>
  <div class="front-mark-dot"></div>
  <div class="front-wordmark">Vellmoor.mx</div>
  <p class="front-cities"><span>MEXICO CITY</span><span>TIJUANA</span><span>SAN DIEGO</span></p>
  <p class="front-follow">Follow us on:</p>
  <ul class="social-list">
    <li>Chatterbox</li><li>Peeplo</li><li>Zenbo+</li><li>Clipwall</li><li>Snapframe</li>
  </ul>
</section>

<section class="card card-back" aria-label="Card back">
  <svg class="back-frame" width="500" height="760" aria-hidden="true">
    <polygon points="0,0 500,0 500,30 250,70 0,30" fill="var(--black)"/>
    <polyline points="0,34 250,74 500,34" stroke="var(--blue)" stroke-width="4" fill="none"/>
    <polygon points="0,760 500,760 500,690 250,640 0,690" fill="var(--black)"/>
    <polyline points="0,686 250,636 500,686" stroke="var(--blue)" stroke-width="4" fill="none"/>
    <path d="M0 380 L30 380 C50 480 40 580 24 680 L0 684 Z" fill="var(--blue)"/>
    <path d="M500 380 L470 380 C450 480 460 580 476 680 L500 684 Z" fill="var(--blue-deep)"/>
  </svg>
  <div class="back-mark-dot"></div>
  <div class="back-wordmark">Vellmoor.mx</div>
  <p class="person-name">Tomas Emil Varga</p>
  <p class="person-surname">Lindqvist</p>
  <div class="divider" style="top:484px"></div>
  <p class="contact-line" style="top:500px">
    <svg class="phone-icon" width="16" height="22" viewBox="0 0 16 22" aria-hidden="true">
      <rect x="1" y="1" width="14" height="20" rx="3" fill="var(--orange)"/>
      <rect x="4" y="4" width="8" height="12" fill="var(--white)"/>
    </svg>+5219987350418
  </p>
  <p class="contact-line" style="top:530px"><span class="label">USA Number:</span> 1-800-572-9183</p>
  <div class="divider" style="top:572px"></div>
  <p class="contact-line contact-small" style="top:590px"><span class="label">VuCall &amp; QuickNote:</span> studio@vellmoor-example.mx</p>
  <p class="contact-line contact-small" style="top:616px"><span class="label">Talkwave:</span> studiovellmoormx</p>
</section>

</body>
</html>
```